Stationery Design Project

Require letterhead/stationery design based on new logo (see attached).

Would prefer it kept simple but strong and effective.

Target Market(s)

Clients and building developers. Residential/consumer and corporate clientele.

```html
<!DOCTYPE html>
<html lang="en">
<head>
<meta charset="utf-8">
<title>Keystrand Projects – Letterhead</title>
<link rel="stylesheet" href="https://fonts.googleapis.com/css2?family=Open+Sans:wght@400&display=swap">
<style>
  :root {
    --paper: #ffffff;
    --brand-blue: #29abe2;
    --brand-grey: #6d6e71;
    --text-dark: #4d4d4f;
    --decor-tint: #eaf6fb;
  }
  html, body {
    margin: 0;
    padding: 0;
    overflow: hidden;
    background: var(--paper);
  }
  .letterhead {
    position: relative;
    width: 848px;
    height: 1200px;
    overflow: hidden;
    background: var(--paper);
    font-family: "Open Sans", Arial, sans-serif;
  }
  .brand {
    position: absolute;
    top: 60px;
    right: 70px;
    width: 170px;
    display: flex;
    flex-direction: column;
    align-items: center;
  }
  .brand-square {
    width: 74px;
    height: 74px;
    background: var(--brand-blue);
    margin-bottom: 18px;
  }
  .brand-name {
    margin: 0;
    font-weight: 400;
    font-size: 22px;
    line-height: 1.15;
    letter-spacing: 1px;
    color: var(--brand-grey);
    text-align: center;
    text-transform: uppercase;
  }
  .brand-name .brand-sub {
    display: block;
    font-size: 11px;
    letter-spacing: 7px;
    margin-right: -7px;
  }
  .corner-decor {
    position: absolute;
    left: 0;
    bottom: 0;
    width: 400px;
    height: 470px;
  }
  .contact {
    position: absolute;
    left: 425px;
    width: 360px;
    top: 1060px;
    font-size: 14px;
    line-height: 21px;
  }
  .contact-row {
    display: flex;
    justify-content: space-between;
    color: var(--brand-blue);
  }
  .contact-phone { justify-content: flex-end; }
  .contact-address {
    margin-top: 22px;
    color: var(--text-dark);
  }
</style>
</head>
<body>
  <main class="letterhead">
    <header class="brand">
      <div class="brand-square"></div>
      <h1 class="brand-name">Keystrand<span class="brand-sub">Projects</span></h1>
    </header>

    <svg class="corner-decor" viewBox="0 0 400 470" aria-hidden="true">
      <circle cx="140" cy="270" r="250" fill="var(--decor-tint)"/>
    </svg>

    <footer class="contact">
      <div class="contact-row contact-phone"><span>+1 234 567 89 00</span></div>
      <div class="contact-row">
        <span>www.yourwebsite.com</span>
        <span>info@emailaddress.com</span>
      </div>
      <div class="contact-address">physical address and location related information here</div>
    </footer>
  </main>
</body>
</html>
```